Quilting Template Retail Label

These are laser cut acrylic templates used to trace shapes onto fabrics. Quilters use these to make repeatable cuts quickly and accurately. Sometimes referred to as quilt rulers. I need to make a label design for my line of products that shows the quality and elegance of these templates. It needs to be an eye catching design as there is stiff competition for the attention of shoppers. Feminine colors are also preferred.

The reference design will be for an item called a "Drunkards Path 7" & 3.5" Set". The label should also say "4 piece set". The brand name is Every Plain Polymer. The Drunkards Path is essentially a Square with a quarter of a circle cut out of it. I would like a dashed line border offset from the edge of the label, that represents the seam allowance. The seam allowance is engraved on all templates.

Pictures of the items are attached, as well as pictures of labels that I would like you to use for inspiration. The picture of the quilt is one of the designs that can be made with the Drunkards Path template. Lastly, there are pictures of the pegboards in shops where these will be displayed, this should give you an idea of the competition.

Target Market(s)

Quilters, older women, affluent

Industry/Entity Type

Retail

Colors
e34297
e667a6
b868aa
d2a4cc

Requirements
Must have
• Must be elegant and give the feeling of a quality product.

```html
<!DOCTYPE html>
<html lang="en">
<head>
<meta charset="utf-8">
<title>Drunkards Path Template Label</title>
<link rel="stylesheet" href="https://fonts.googleapis.com/css2?family=Alegreya:wght@700;900&display=swap">
<style>
  :root {
    --page-bg: #eeeeee;
    --label-pink: #f2a6c9;
    --pattern-hot: #e34297;
    --pattern-rose: #e667a6;
    --pattern-plum: #b868aa;
    --pattern-lilac: #d2a4cc;
    --pattern-mint: #c6dcd2;
    --pattern-cream: #efe6dc;
    --frame-red: #d93a52;
    --panel-white: #f5f3f4;
    --seam-red: #b01e35;
    --brand-red: #d63a55;
    --title-plum: #7b2a74;
    --title-outline: #b8b2a0;
    --ribbon-light: #d43a50;
    --ribbon-dark: #8e1424;
    --badge-ink: #8c1020;
    --badge-red: #c01a32;
  }
  html, body {
    margin: 0;
    width: 1200px;
    height: 1200px;
    overflow: hidden;
    background: var(--page-bg);
  }
  .label {
    position: absolute;
    left: 20px;
    top: 166px;
    width: 1160px;
    height: 868px;
    display: block;
  }
  .label-text {
    font-family: "Alegreya", Georgia, serif;
    text-anchor: middle;
  }
  .brand-name { font-weight: 700; fill: var(--brand-red); font-size: 92px; }
  .product-title {
    font-weight: 900; font-size: 104px; fill: var(--title-plum);
    stroke: var(--title-outline); stroke-width: 3; paint-order: stroke;
  }
  .product-sizes { font-weight: 900; font-size: 60px; fill: var(--title-plum); }
  .badge-count { font-weight: 900; font-size: 96px; fill: var(--badge-ink); }
  .badge-caption { font-weight: 900; font-size: 36px; fill: var(--badge-red); }
</style>
</head>
<body>
<svg class="label" viewBox="0 0 1297 970" xmlns="http://www.w3.org/2000/svg">
  <defs>
    <linearGradient id="pattern-tones" x1="0" y1="0" x2="0" y2="1">
      <stop offset="0" stop-color="#e667a6"/>
      <stop offset="0.1" stop-color="#ec8a9a"/>
      <stop offset="0.2" stop-color="#d9c9cc"/>
      <stop offset="0.3" stop-color="#d2a4cc"/>
      <stop offset="0.4" stop-color="#b868aa"/>
      <stop offset="0.5" stop-color="#e3a8bf"/>
      <stop offset="0.6" stop-color="#e34297"/>
      <stop offset="0.7" stop-color="#d9c9cc"/>
      <stop offset="0.8" stop-color="#b868aa"/>
      <stop offset="0.9" stop-color="#e34297"/>
      <stop offset="1" stop-color="#c6dcd2"/>
    </linearGradient>
    <radialGradient id="ribbon-tones" cx="0.5" cy="0.45" r="0.6">
      <stop offset="0" stop-color="var(--ribbon-light)"/>
      <stop offset="1" stop-color="var(--ribbon-dark)"/>
    </radialGradient>
    <path id="frame-shape" d="M 300 160 Q 648 70 996 160 L 1000 240 L 1100 240 L 1100 310 Q 1215 330 1222 450 Q 1215 570 1100 590 L 1100 650 L 1000 650 L 996 730 Q 648 700 300 730 L 296 650 L 196 650 L 196 590 Q 81 570 74 450 Q 81 330 196 310 L 196 240 L 296 240 Z"/>
  </defs>

  <rect class="label-base" width="1297" height="970" fill="var(--label-pink)"/>
  <rect class="chevron-band" x="28" y="25" width="1244" height="910" fill="url(#pattern-tones)" role="img" aria-label="Rows of pink, purple, mint and cream triangle chevrons"/>

  <g class="title-frame">
    <use href="#frame-shape" fill="var(--frame-red)"/>
    <use href="#frame-shape" fill="var(--panel-white)" transform="translate(648 445) scale(0.94 0.9) translate(-648 -445)"/>
    <use href="#frame-shape" fill="none" stroke="var(--seam-red)" stroke-width="2.5" stroke-dasharray="14 9" transform="translate(648 445) scale(0.89 0.82) translate(-648 -445)"/>
  </g>

  <text class="label-text brand-name" x="648" y="300">Every Plain</text>
  <text class="label-text brand-name" x="648" y="390">Polymer</text>
  <text class="label-text product-title" x="648" y="527">Drunkards Path</text>
  <text class="label-text product-sizes" x="648" y="620">7" &amp; 3.5" Set</text>

  <ellipse class="bow-ribbon" cx="648" cy="785" rx="330" ry="110" fill="url(#ribbon-tones)" role="img" aria-label="Red satin ribbon bow tied beneath the title frame"/>

  <g class="piece-badge">
    <circle cx="645" cy="780" r="106" fill="var(--frame-red)"/>
    <circle cx="645" cy="780" r="96" fill="var(--panel-white)"/>
    <text class="label-text badge-count" x="645" y="778">4</text>
    <text class="label-text badge-caption" x="645" y="818">PIECE</text>
    <text class="label-text badge-caption" x="645" y="852">SET</text>
  </g>
</svg>
</body>
</html>
```